4 panel (or page) brochure

We need a brochure design for a Oklahoma based company. We manufacture and sell underground and below ground shelters. We sell our shelters in our local showroom, as well distribute our shelters to a big box national retailer. I would like to have a simple design that includes a few pictures of our product and details on each product we offer as well as install details for each product. Our out of state retailers likely will not have our product display so we will need something that sells the product without seeing it in person.

I would like something that it easily printable as well as able to edit at a later time if needed.

I've included Catalog/Brochure Copy
Pictures of Below Ground Units/Above Ground Units - feel free to edit or touch up.
Some brochure ideas I found on SketchForum that seemed to be similar to what we can do.
The Inside of a brochure we did a while back that we liked (style-wise)
A general info flyer for more information

```html
<!DOCTYPE html>
<html lang="en">
<head>
<meta charset="utf-8">
<title>Storm Shelter Brochure – Inside Spread</title>
<link href="https://fonts.googleapis.com/css2?family=Source+Sans+3:wght@400;600;700&family=Libre+Baskerville&display=swap" rel="stylesheet">
<style>
:root{
  --backdrop:#4a4a4a;
  --brand-red:#b2202a;
  --brand-red-dark:#9c1a23;
  --ink:#1c1c1c;
  --rule-dark:#1a1a1a;
  --paper-light:#ffffff;
  --paper-grey:#cfcfd1;
  --table-a:#d9d9d9;
  --table-b:#ececec;
  --photo-frame:#2a2a2a;
}
*{margin:0;padding:0;box-sizing:border-box}
html,body{width:1200px;height:874px;overflow:hidden;background:var(--backdrop)}
body{font-family:"Source Sans 3",sans-serif;position:relative}
.spread{position:absolute;left:26px;top:45px;width:1151px;height:745px}
.page{position:absolute;top:0;height:745px;overflow:hidden}
.page--left{left:0;width:574px}
.page--right{left:574px;width:577px}

.band{position:absolute;left:0;width:100%}
.band--red{background:linear-gradient(90deg,var(--brand-red-dark),var(--brand-red) 60%,var(--brand-red-dark))}
.band--light-left{background:linear-gradient(90deg,#e4e4e6 0%,#ffffff 35%,#f4f4f5 65%,var(--paper-grey) 100%)}
.band--light-right{background:linear-gradient(90deg,#ffffff 0%,#f4f4f5 55%,#d6d6d8 100%)}
.divider{position:absolute;left:0;width:100%;height:3px;background:var(--rule-dark)}

.abs{position:absolute}
.heading{font-weight:600;font-size:15px;letter-spacing:.2px}
.heading--light{color:#fff}
.heading--dark{color:var(--ink);font-weight:700}
.rule{position:absolute;height:1.5px}
.rule--light{background:#f0d6d6}
.rule--red{background:var(--brand-red)}

.cert-list{list-style:none;color:#fff;font-size:11px;line-height:22px}
.cert-list li::before{content:"•";margin-right:6px}
.upgrade-list{list-style:none;color:#fff;font-size:11px;line-height:15.6px}
.note{color:#fff;font-size:11px;line-height:15.6px;width:470px}

.faq{width:490px;font-size:11px;line-height:15.5px;color:var(--ink)}
.faq dt{color:var(--brand-red);font-weight:700;margin-bottom:4px}
.faq dd{margin-bottom:16px}

.title{color:var(--brand-red);font-weight:700;font-size:23px;letter-spacing:.2px}
.intro{width:238px;font-size:11.5px;line-height:18.9px;color:var(--ink);text-align:justify}

.photo{position:absolute}
.photo--framed{border:3px solid var(--photo-frame);background:linear-gradient(180deg,#3a4a7a 0%,#d9dbe0 12%,#f4f4f4 50%,#c8c8c8 100%)}
.photo--white{border:3px solid #f2f2f2;background:linear-gradient(160deg,#d0d2d4 0%,#f2f2f0 40%,#cfcfcd 100%)}

.sizes{position:absolute;border-collapse:collapse;font-family:"Libre Baskerville",serif;font-size:10.5px;color:var(--ink)}
.sizes th,.sizes td{width:110px;height:21px;text-align:center;font-weight:400}
.sizes th{font-weight:700;background:var(--table-a)}
.sizes tr:nth-child(odd) td{background:var(--table-a)}
.sizes tr:nth-child(even) td{background:var(--table-b)}

.spec-list{list-style:none;color:#fff;font-size:11px;line-height:18.3px}
.spec-list li::before{content:"•";margin-right:6px}
</style>
</head>
<body>
<div class="spread">

  <section class="page page--left">
    <div class="band band--red" style="top:0;height:307px"></div>
    <div class="divider" style="top:307px"></div>
    <div class="band band--light-left" style="top:310px;height:435px"></div>

    <h2 class="abs heading heading--light" style="left:27px;top:20px">CERTIFICATION:</h2>
    <div class="rule rule--light" style="left:27px;top:44px;width:227px"></div>
    <ul class="abs cert-list" style="left:28px;top:48px">
      <li>Exceeds FEMA 320/361 guidelines for storm shelter</li>
      <li>Exceeds ICC-500 guidelines for storm shelters</li>
    </ul>
    <ul class="abs cert-list" style="left:320px;top:48px">
      <li>Tested at Plains Tech University</li>
      <li>FEMA Compliant</li>
    </ul>

    <h2 class="abs heading heading--light" style="left:27px;top:116px">BELOW GROUND SHELTER UPGRADES:</h2>
    <div class="rule rule--light" style="left:27px;top:140px;width:272px"></div>
    <ul class="abs upgrade-list" style="left:28px;top:152px">
      <li>Metal steps &amp; benches&nbsp; $150</li>
      <li>8” wide wooden, carpeted steps&nbsp; $100 (standard size is 6”)</li>
      <li>10” wide wooden, carpeted benches $165</li>
      <li>Extra Handrail $50</li>
      <li>Hole for electric boxes $75</li>
      <li>Outside lock for lid $60</li>
    </ul>
    <p class="abs note" style="left:28px;top:261px">As an upgrade our In-ground shelters can also be installed outside with our specially designed outside lid.&nbsp; Ask associate for outside lid upgrade pricing.</p>

    <h2 class="abs heading heading--dark" style="left:27px;top:342px">BELOW GROUND SHELTERS FAQ:</h2>
    <div class="rule rule--red" style="left:27px;top:365px;width:279px"></div>
    <dl class="abs faq" style="left:28px;top:380px">
      <dt>Q)&nbsp; Can I park on my below ground shelter?</dt>
      <dd>Yes, you can park on our shelters.&nbsp; Our shelters have been designed to be durable and can withstand the weight of your vehicle. We do recommend parking in a position where your car straddles the lid of the shelter.</dd>
      <dt>Q)&nbsp; Can I get trapped in my shelter?</dt>
      <dd>Our locking mechanism is simple yet sturdy and secure. The bearing we have to support our door is the most durable on the market. Our shelters are impact tested and our bearings our not likely to bust in the event of a tornado. If something extremely heavy is on the door you can open the shelter with a&nbsp; one-ton come along. The lid is also built with a secondary emergency exit that can be opened with the help of a jack.</dd>
      <dt>Q)&nbsp; Will there be a mess?</dt>
      <dd>We use a wet saw to cut the concrete so there will be no concrete dust. After the install is complete we power wash the work area as well as the driveway.&nbsp; In most cases, the area is cleaner than when we arrive.</dd>
      <dt>Q)&nbsp; Will the shelter look flat once its installed?</dt>
      <dd>Yes, the shelter will actually stand a 1/4 of an inch over the original slab to prevent water from going into the shelter.&nbsp; However, our concrete experts will grade the concrete around the slab so that it looks flat.&nbsp; This allows water to run away from the shelter.</dd>
    </dl>
  </section>

  <section class="page page--right">
    <div class="band band--light-right" style="top:0;height:445px"></div>
    <div class="divider" style="top:445px"></div>
    <div class="band band--red" style="top:448px;height:297px"></div>

    <h1 class="abs title" style="left:16px;top:14px">ABOVE GROUND SAFE ROOMS</h1>
    <p class="abs intro" style="left:19px;top:56px">Our above ground shelters are engineered, tested and meet the highest quality standards at a competitive price.&nbsp; Our shelters come in a variety of sizes ranging from 3-4 people to 16-20 people. Our above ground shelters are built stronger than our competitors using a minimum of 3/16” steel, are fully painted inside and out and are made to withstand 260 mph winds. All units also come standard with a&nbsp; bullet proof lookout glass window. Our safe rooms are FEMA compliant and are built using FEMA publications 320 guidelines.</p>

    <div class="photo photo--framed" role="img" aria-label="White steel above ground safe room with closed door and lookout window, in a showroom" style="left:282px;top:75px;width:285px;height:327px"></div>

    <h2 class="abs heading heading--dark" style="left:15px;top:296px">SAFE ROOM SIZES</h2>
    <div class="rule rule--red" style="left:15px;top:319px;width:222px"></div>
    <table class="sizes" style="left:17px;top:321px">
      <tr><th>Size</th><th>Fits</th></tr>
      <tr><td>3x5 or 4x4</td><td>2-4 people</td></tr>
      <tr><td>4x6</td><td>4-6 people</td></tr>
      <tr><td>4x8</td><td>6-8 people</td></tr>
      <tr><td>5x7</td><td>8-10 people</td></tr>
    </table>

    <div class="photo photo--white" role="img" aria-label="Open safe room door showing the white painted interior" style="left:16px;top:482px;width:148px;height:234px"></div>

    <h2 class="abs heading heading--light" style="left:214px;top:460px">SPECIFICATIONS</h2>
    <div class="rule rule--light" style="left:214px;top:483px;width:272px"></div>
    <ul class="abs spec-list" style="left:216px;top:492px">
      <li>3/16” steel plates for exterior skin</li>
      <li>Solid welds</li>
      <li>2” x 2” x ¼” square tubing for internal subframe</li>
      <li>3”x3”x ¼” angle iron for bottom frame</li>
      <li>8” custom designed air vents</li>
      <li>3 BHMA/ANSI Grade 1 Dead bolt locking system</li>
      <li>Concrete anchoring system</li>
      <li>Bullet proof window comes standard with every shelter</li>
      <li>Double-skinned door (3/16” exterior plate and 12 gauge interior sheet</li>
      <li>3 heavy duty removable steel door hinges</li>
      <li>24” wide door</li>
      <li>Door opens to the inside to keep debris from blocking door</li>
      <li>Door is removable in case of emergency</li>
    </ul>
  </section>

</div>
</body>
</html>
```